Plume - Stationary Design/Layout

We are a well established clothing design and manufacturing company (Plume Sourcing) based in London UK, with our own factory in Bangladesh, supplying to many fashion retailers and brands. Our factory has very high environmental and ethical standards with people at its heart. Our quality of garments are second to none.
Our new logo has been proudly developed by the Pixel Guild community last month, we are now in the second phase and need the layout designed for our letterheads, double sided business cards, compliment slip and clothing ticket. Feel as creative as you like, but make sure it looks great!!
***The Logo - the logo design and colour is set and should NOT be changed and stay on a dark grey backround. The logo artwork to use is attached.
***Details to use for the business card:
Dorian Hartley
Direct Line: 020 7946 0518
dorian@plumesourcing-mail.test
Plume Sourching Ltd.
58 - 60 Fenwick Row
Harrowby . Kelsworth
NW3 5QJ
Switchboard: 020 7946 0733
Fax: 020 7946 0733
www.plumesourcing-mail.test
***Details to use for the letterhead and compliment slip:
Plume Sourching Ltd.
58 - 60 Fenwick Row
Harrowby . Kelsworth
NW3 5QJ
Fax: 020 7946 0733
www.plumesourcing-mail.test
***Details for Swing Ticket:
Size: 12cm height by 5.5cm width
One side need to have just the logo without the 'Sourcing', on the other it needs to stay blank

```html
<!DOCTYPE html>
<html lang="en">
<head>
<meta charset="utf-8">
<title>Plume Sourcing – Business Card</title>
<link rel="stylesheet" href="https://fonts.googleapis.com/css2?family=Questrial&display=swap">
<style>
  :root {
    --aqua: #aee0e5;
    --charcoal: #3c3c3c;
    --paper: #ffffff;
    --ink: #3a3a3a;
    --muted: #9a9a9a;
    --edge: #cfcfcf;
    --backdrop: #f1f1f1;
  }
  * { margin: 0; padding: 0; box-sizing: border-box; }
  html, body { width: 1200px; height: 900px; overflow: hidden; }
  body {
    position: relative;
    background: var(--backdrop);
    font-family: "Questrial", "Century Gothic", sans-serif;
    color: var(--ink);
  }
  .card-shapes { position: absolute; inset: 0; }
  .brand {
    position: absolute;
    right: calc(1200px - 483px);
    top: 384px;
    text-align: right;
    color: var(--aqua);
    line-height: 1;
    text-transform: uppercase;
  }
  .brand-name { display: block; font-size: 80px; letter-spacing: 3px; margin-right: -3px; }
  .brand-sub { display: block; font-size: 25px; letter-spacing: 0.5px; margin-top: -4px; }
  .brand-web {
    position: absolute;
    left: 150px;
    width: 333px;
    top: 498px;
    font-size: 11.5px;
    letter-spacing: 3px;
    color: var(--muted);
    text-align: right;
    white-space: nowrap;
  }
  .company {
    position: absolute;
    left: 637px;
    top: 423px;
    font-size: 13px;
    line-height: 21px;
    font-style: normal;
    white-space: nowrap;
  }
  .company-name { color: var(--aqua); }
  .person {
    position: absolute;
    left: 805px;
    top: 383px;
  }
  .person-name { font-size: 22px; font-weight: normal; color: var(--ink); margin-bottom: 8px; }
  .contact-list { list-style: none; font-size: 13px; }
  .contact-list li {
    display: flex;
    align-items: center;
    height: 25px;
    white-space: nowrap;
  }
  .contact-list li::before {
    content: "";
    width: 6px;
    height: 6px;
    border: 2px solid var(--aqua);
    border-radius: 50%;
    margin-right: 5px;
  }
</style>
</head>
<body>
  <svg class="card-shapes" width="1200" height="900" viewBox="0 0 1200 900" aria-hidden="true">
    <path d="M212 300 H395 V596 H212 A148 148 0 0 1 212 300 Z" fill="var(--aqua)"/>
    <path d="M395 300 H567 A20 20 0 0 1 587 320 V576 A20 20 0 0 1 567 596 H395 Z" fill="var(--charcoal)"/>
    <path d="M201 363 H400 V535 H201 A86 86 0 0 1 201 363 Z" fill="var(--charcoal)"/>
    <path d="M806 300 H631 A20 20 0 0 0 611 320 V576 A20 20 0 0 0 631 596 H806" fill="var(--paper)" stroke="var(--edge)" stroke-width="1"/>
    <path d="M804 300 H996 A148 148 0 0 1 996 596 H804 Z" fill="var(--aqua)"/>
    <path d="M800 363 H982 A86 86 0 0 1 982 535 H800 Z" fill="var(--paper)"/>
  </svg>

  <section class="card-front">
    <div class="brand">
      <span class="brand-name">Plume</span>
      <span class="brand-sub">Sourcing</span>
    </div>
    <p class="brand-web">www.plumesourcing-mail.test</p>
  </section>

  <section class="card-back">
    <address class="company">
      <div class="company-name">Plume Sourching Ltd.</div>
      <div>58 – 60 Fenwick Row</div>
      <div>Harrowby . Kelsworth</div>
      <div>NW3 5QJ</div>
    </address>
    <div class="person">
      <h1 class="person-name">Dorian Hartley</h1>
      <ul class="contact-list">
        <li>Direct Line: 020 7946 0518</li>
        <li>dorian@plumesourcing-mail.test</li>
        <li>Switchboard: 020 7946 0733</li>
        <li>Fax: 020 7946 0733</li>
      </ul>
    </div>
  </section>
</body>
</html>
```